Business Card Design for an Investment Company

We need a business card design for our private investment company, called Ashbourne Partners. Ashbourne Partners is an investments partnership that aims to acquire shares in listed companies with a view to influencing those companies through active dialogue in order to improve their value. We need designs that use the logo colors (blue, grey, white), we need both English and Arabic on the business cards (can be on one side or 2 sides). The final logo should communicate professionalism, conservatism (nothing too fancy or too cheesy), that we are smart, conservative and old school.

Target Market(s)

Investment companies

Industry/Entity Type

Investment

Contact Information for Business Card

Khalid Yousef Rumaithi
Senior Executive Officer

Palm Terrace 07, Level 3, Office 215/12
HLMZ

+9714987650
krumaithi@ashbournepartners.com
www.ashbournepartners.com

Requirements
Must have
• Logo to be placed on the left hand side of the business card
• for the Arabic, we only need to have the name and title so it can be accomodated on one side so we can have the other side with full color and logo. The arabic that needs to be used is the below:
• خالد يوسف الرميثي
• المدير التنفيدي

```html
<!DOCTYPE html>
<html lang="en">
<head>
<meta charset="utf-8">
<title>Ashbourne Partners — Business Card</title>
<link rel="stylesheet" href="https://fonts.googleapis.com/css2?family=Lato:wght@400;700;900&family=Noto+Kufi+Arabic:wght@400;700&display=swap">
<style>
  :root {
    --brand-blue: #1670a3;
    --brand-grey: #4a4a4c;
    --ink: #1e1e20;
    --paper: #fbfbfb;
    --backdrop: #6a6870;
    --rule: #55555a;
  }
  * { margin: 0; padding: 0; box-sizing: border-box; }
  html, body {
    width: 1200px; height: 675px; overflow: hidden;
    background: var(--backdrop);
    font-family: "Lato", Arial, sans-serif;
  }
  .stage {
    position: relative; width: 1200px; height: 675px;
    display: flex; align-items: center; justify-content: center; gap: 30px;
  }
  .card {
    position: relative; width: 540px; height: 309px;
    box-shadow: 0 6px 18px rgba(0,0,0,0.35);
    overflow: hidden;
  }
  .card--front { background: var(--paper); color: var(--ink); }
  .card--back {
    background: var(--brand-blue);
    display: flex; align-items: center; justify-content: center;
  }
  .wordmark {
    font-weight: 900; letter-spacing: -0.5px; line-height: 1;
    white-space: nowrap;
  }
  .card--front .wordmark {
    position: absolute; top: 62px; left: 44px;
    font-size: 34px; color: var(--brand-blue);
  }
  .card--back .wordmark { font-size: 40px; color: #ffffff; }
  .edge-tab { position: absolute; width: 9px; height: 58px; }
  .edge-tab--blue { left: 0; top: 222px; background: var(--brand-blue); }
  .edge-tab--grey { right: 0; top: 38px; background: var(--brand-grey); }
  .divider {
    position: absolute; left: 292px; top: 150px;
    width: 1px; height: 110px; background: var(--rule);
  }
  .person {
    position: absolute; left: 44px; width: 228px; text-align: right;
  }
  .person--arabic {
    top: 150px; direction: rtl; text-align: left;
    font-family: "Noto Kufi Arabic", Tahoma, sans-serif;
  }
  .person--english { top: 222px; }
  .person--arabic .person__name { font-size: 13px; line-height: 1.5; }
  .person--arabic .person__title { font-size: 11.5px; line-height: 1.5; margin-top: 0; }
  .person__name { font-size: 13px; font-weight: 700; color: var(--brand-blue); }
  .person__title { font-size: 12.5px; color: var(--brand-grey); margin-top: 1px; }
  .contact { position: absolute; left: 312px; top: 150px; width: 222px; }
  .contact__address { font-size: 8.5px; line-height: 1.25; color: var(--ink); margin-bottom: 8px; }
  .contact__row {
    display: flex; align-items: center; gap: 8px;
    font-size: 11px; line-height: 1.5; color: var(--ink); white-space: nowrap;
  }
  .contact__row svg { width: 10px; height: 10px; flex: none; fill: var(--ink); }
</style>
</head>
<body>
<main class="stage">
  <section class="card card--front" aria-label="Card front">
    <div class="wordmark">Ashbourne Partners</div>
    <span class="edge-tab edge-tab--grey"></span>
    <span class="edge-tab edge-tab--blue"></span>
    <div class="divider"></div>
    <div class="person person--arabic" lang="ar">
      <p class="person__name">خالد يوسف الرميثي</p>
      <p class="person__title">المدير التنفيدي</p>
    </div>
    <div class="person person--english">
      <p class="person__name">Khalid Yousef Rumaithi</p>
      <p class="person__title">Senior Executive Officer</p>
    </div>
    <div class="contact">
      <p class="contact__address">Palm Terrace 07, Level 3, Office 215/12<br>HLMZ</p>
      <p class="contact__row">
        <svg viewBox="0 0 10 10" aria-hidden="true"><path d="M2 0.5 3.6 2.6 2.7 3.6C3.3 5 4.9 6.7 6.4 7.3L7.4 6.4 9.5 8 8.6 9.4C4.6 9.2 0.8 5.4 0.6 1.4Z"/></svg>
        +9714987650
      </p>
      <p class="contact__row">
        <svg viewBox="0 0 10 10" aria-hidden="true"><path d="M0.5 2H9.5V8H0.5Z M1.2 2.6 5 5.6 8.8 2.6" fill="none" stroke="#1e1e20" stroke-width="1"/></svg>
        krumaithi@ashbournepartners.com
      </p>
      <p class="contact__row">
        <svg viewBox="0 0 10 10" aria-hidden="true"><g fill="none" stroke="#1e1e20" stroke-width="0.9"><circle cx="5" cy="5" r="4.3"/><ellipse cx="5" cy="5" rx="1.8" ry="4.3"/><path d="M0.7 5H9.3M1.4 2.8H8.6M1.4 7.2H8.6"/></g></svg>
        www.ashbournepartners.com
      </p>
    </div>
  </section>
  <section class="card card--back" aria-label="Card back">
    <div class="wordmark">Ashbourne Partners</div>
  </section>
</main>
</body>
</html>
```